Marist District College Brenthollow Letterhead

Our college is called Marist District College Brenthollow. We would like to request a few letterhead design options to choose from please. We look forward to seeing some new and fresh ideas for our College Letterhead.

Please note that the College has the following PMS Colours:
MAROON – PMS 229C
BLUE – PMS 2747C
GOLD – PMS 871C
YELLOW – PMS 123C

Our College Motto is:
Light guiding Purpose.
I have attached a copy of our current letterhead and College Logo.

Please note that the letterhead must include the following details:

Marist District College Brenthollow
Light Guiding Purpose
Phone: 9472 0000
Fax:9481 3157
Address: 517 Brenthollow Road Brenthollow 3037
Mail:PO BOX 4817 Wattle Bend VIC 3038 Australia
ABN 47 816 205 938

www.mdcbrenthollow-example.net
https://twitter.com/mdcbrenthollow
https://www.pinterest.com/mdcbrenthollow
https://www.facebook.com/MDCBrenthollow
www.videohub-example.com (search MDC Brenthollow)

Please feel free to contact me on the below detail if I can further assist.

Regards,
Joanna Verkuil
reception@mdcbrenthollow-example.net
PH: 9472 0000

Target Market(s)

College Community

Industry/Entity Type

Education

Requirements
Must have
• See Project Description
Nice to have
• see Project Description

```html
<!DOCTYPE html>
<html lang="en">
<head>
<meta charset="utf-8">
<title>Marist District College Brenthollow Letterhead</title>
<link href="https://fonts.googleapis.com/css2?family=Open+Sans:wght@400;600;700&display=swap" rel="stylesheet">
<style>
  :root {
    --maroon: #6e2145;
    --blue: #2b3a8c;
    --gold: #8c6d43;
    --yellow: #f6c21a;
    --paper: #ffffff;
    --ink-light: #f4ecdf;
    --watermark: #ece6de;
    --watermark-circle: #d9dce9;
  }
  html, body {
    margin: 0;
    padding: 0;
    overflow: hidden;
    background: var(--paper);
  }
  .sheet {
    position: relative;
    width: 841px;
    height: 1200px;
    overflow: hidden;
    background: var(--paper);
    font-family: "Open Sans", Arial, sans-serif;
  }
  .header-band {
    position: absolute;
    left: 0;
    top: 10px;
    width: 841px;
    height: 175px;
    background: var(--gold);
  }
  .college-name {
    position: absolute;
    left: 40px;
    top: 26px;
    margin: 0;
    font-size: 25px;
    font-weight: 700;
    color: var(--maroon);
    letter-spacing: 0.2px;
  }
  .motto {
    position: absolute;
    left: 40px;
    top: 62px;
    margin: 0;
    display: flex;
    align-items: center;
    gap: 8px;
    font-size: 15px;
    font-weight: 600;
    color: var(--ink-light);
  }
  .contact-row {
    position: absolute;
    left: 40px;
    display: flex;
    align-items: center;
    gap: 14px;
    margin: 0;
    padding: 0;
    list-style: none;
    font-size: 10.5px;
    color: var(--ink-light);
    white-space: nowrap;
  }
  .contact-row li {
    display: flex;
    align-items: center;
    gap: 5px;
  }
  .row-address { top: 92px; }
  .row-phone { top: 118px; }
  .row-online { top: 146px; gap: 10px; font-size: 10px; }
  .dot {
    display: inline-block;
    width: 13px;
    height: 13px;
    border-radius: 50%;
    background: var(--yellow);
    flex: none;
  }
  .brand-mark {
    position: absolute;
    left: 676px;
    top: 18px;
    width: 130px;
    text-align: center;
  }
  .brand-mark .brand-circle {
    display: block;
    width: 96px;
    height: 96px;
    margin: 0 auto 8px;
    border-radius: 50%;
    background: var(--maroon);
  }
  .brand-mark .brand-name {
    font-size: 13px;
    font-weight: 700;
    color: var(--ink-light);
    line-height: 1.2;
  }
  .watermark {
    position: absolute;
    left: 270px;
    top: 470px;
    width: 300px;
    text-align: center;
  }
  .watermark .watermark-circle {
    display: block;
    width: 170px;
    height: 170px;
    margin: 0 auto 20px;
    border-radius: 50%;
    background: var(--watermark-circle);
    opacity: 0.7;
  }
  .watermark .watermark-name {
    font-size: 24px;
    font-weight: 700;
    color: var(--watermark);
    line-height: 1.25;
  }
</style>
</head>
<body>
<div class="sheet">
  <header class="header-band">
    <h1 class="college-name">Marist District College Brenthollow</h1>
    <p class="motto"><span class="dot"></span>Light Guiding Purpose</p>

    <ul class="contact-row row-address">
      <li><span class="dot"></span>517 Brenthollow Road Brenthollow 3037</li>
      <li><span class="dot"></span>PO BOX 4817 Wattle Bend VIC 3038 Australia</li>
    </ul>

    <ul class="contact-row row-phone">
      <li><span class="dot"></span>Phone: 9472 0000</li>
      <li><span class="dot"></span>Fax: 9481 3157</li>
      <li><span class="dot"></span>ABN 47 816 205 938</li>
    </ul>

    <ul class="contact-row row-online">
      <li><span class="dot"></span>www.mdcbrenthollow-example.net</li>
      <li><span class="dot"></span>/mdcbrenthollow</li>
      <li><span class="dot"></span>/mdcbrenthollow</li>
      <li><span class="dot"></span>/MDCBrenthollow</li>
      <li><span class="dot"></span>www.videohub-example.com (MDC Brenthollow)</li>
    </ul>

    <div class="brand-mark">
      <span class="brand-circle"></span>
      <span class="brand-name">MDC Brenthollow</span>
    </div>
  </header>

  <div class="watermark" aria-hidden="true">
    <span class="watermark-circle"></span>
    <span class="watermark-name">Marist District College Brenthollow</span>
  </div>
</div>
</body>
</html>
```